Company or website name
- Resume for accounting
- Links to the website
- http://www.gestiondelvallenorte.com/#bienvenidos
- Describe your company and organization and target audience
- The web layout is not for a business. This is a personal site that will present my CV. I am an accountant. It would be nice to follow a model like this website: http://www.gestiondelvallenorte.com/#bienvenidos . The main users of the site will be recruiters.
- The design should have the following
- The design must be modern . There must be both personal photos and scenes work as an office and buildings.

```html
<!DOCTYPE html>
<html lang="en">
<head>
<meta charset="utf-8">
<title>Accountant Résumé — Contact</title>
<link href="https://fonts.googleapis.com/css2?family=Crimson+Pro:ital,wght@1,500;1,700&display=swap" rel="stylesheet">
<style>
  :root {
    --ink: #000000;
    --text: #f2f2f2;
    --rule: #3a3a3a;
    --photo-light: #e6e6e6;
    --photo-mid: #5a5a5a;
    --photo-dark: #0a0a0a;
  }
  html, body {
    margin: 0;
    padding: 0;
    overflow: hidden;
    background: var(--ink);
  }
  .page {
    position: relative;
    width: 1200px;
    height: 675px;
    background: var(--ink);
    overflow: hidden;
    font-family: "Crimson Pro", "Constantia", serif;
    color: var(--text);
  }
  .side-rule {
    position: absolute;
    left: 45px;
    top: 0;
    width: 3px;
    height: 675px;
    background: linear-gradient(to bottom, #111 0%, var(--rule) 40%, var(--rule) 70%, #111 100%);
  }
  .building-photo {
    position: absolute;
    left: 0;
    top: 0;
    width: 1200px;
    height: 675px;
  }
  .main-nav {
    position: absolute;
    left: 60px;
    top: 136px;
    width: 130px;
    display: flex;
    flex-direction: column;
    align-items: center;
    gap: 8.5px;
  }
  .main-nav a {
    color: var(--text);
    text-decoration: none;
    font-style: italic;
    font-weight: 500;
    font-size: 14.5px;
    letter-spacing: 1.3px;
    text-transform: uppercase;
    line-height: 18px;
    white-space: nowrap;
  }
  .main-nav a.is-active {
    text-decoration: underline;
    text-underline-offset: 2px;
  }
  .contact-block {
    position: absolute;
    left: 322px;
    top: 457px;
    font-style: italic;
    font-weight: 700;
    font-size: 17.2px;
    letter-spacing: 1.4px;
    text-transform: uppercase;
    line-height: 19px;
    font-variant-numeric: oldstyle-nums;
    white-space: nowrap;
  }
  .contact-block p {
    margin: 0;
  }
  .contact-block .address {
    margin-bottom: 20px;
  }
</style>
</head>
<body>
<div class="page">
  <svg class="building-photo" viewBox="0 0 1200 675" role="img" aria-label="Black and white photo looking up at a glass office tower against a pale sky">
    <defs>
      <linearGradient id="towerTone" x1="0" y1="0" x2="0.35" y2="1">
        <stop offset="0" stop-color="var(--photo-light)"/>
        <stop offset="0.25" stop-color="var(--photo-mid)"/>
        <stop offset="0.6" stop-color="#222"/>
        <stop offset="1" stop-color="var(--photo-dark)"/>
      </linearGradient>
    </defs>
    <polygon points="531,0 1200,0 1200,675 725,675" fill="url(#towerTone)"/>
  </svg>

  <div class="side-rule"></div>

  <nav class="main-nav">
    <a href="#summary">Summary</a>
    <a href="#highlights">Highlits</a>
    <a href="#experience">Experience</a>
    <a href="#education">Education</a>
    <a href="#contact" class="is-active">Contact</a>
  </nav>

  <section class="contact-block" id="contact">
    <p class="address">24 Harbor Lane<br>Westbrook, CA 91020</p>
    <p>(555) 418-2096<br>hello@ledgerline.net</p>
  </section>
</div>
</body>
</html>
```